Stonewell Holdings

Professional looking business card using darker colours
I do not yet have a logo for the company so feel free to suggest
The business is based on consultancy and project management
Based in Melbourne
Business card can omit the word "Holdings" and can be Stonewell consulting etc.

Contact Name on card : Ravi Pelunkoda Contact number : +61433 512 604 Email address will be confirmed shortly.

```html
<!DOCTYPE html>
<html lang="en">
<head>
<meta charset="utf-8">
<title>Stonewell Consulting — Business Card</title>
<link href="https://fonts.googleapis.com/css2?family=Open+Sans:wght@400;600&display=swap" rel="stylesheet">
<style>
  :root {
    --backdrop: #2b2623;
    --card: #151515;
    --card-edge: #0a0a0a;
    --brand-blue: #3f82d6;
    --silver: #b9b9b9;
    --text-light: #f2f2f2;
  }
  * { margin: 0; padding: 0; box-sizing: border-box; }
  html, body {
    width: 1200px; height: 844px; overflow: hidden;
    background: var(--backdrop);
    font-family: "Open Sans", Arial, sans-serif;
  }
  .stage {
    position: relative; width: 1200px; height: 844px;
    display: flex; align-items: center; justify-content: center; gap: 50px;
  }
  .card {
    position: relative; width: 520px; height: 300px;
    background: var(--card);
    border: 1px solid var(--card-edge);
    box-shadow: 0 10px 30px rgba(0,0,0,.45);
  }
  .brand {
    display: flex; align-items: center; gap: 12px;
    font-weight: 600; letter-spacing: 1px; text-transform: uppercase;
    white-space: nowrap;
  }
  .brand-mark { width: 22px; height: 22px; flex: none; }
  .card-front .brand {
    position: absolute; left: 40px; top: 52px;
    color: var(--brand-blue); font-size: 24px;
  }
  .card-front .brand-mark { background: var(--brand-blue); }
  .contact {
    position: absolute; left: 74px; top: 112px;
    color: var(--text-light); font-size: 14px; line-height: 1.4;
  }
  .contact-name { color: var(--brand-blue); font-weight: 600; font-size: 17px; }
  .contact-role { font-size: 13px; margin-bottom: 4px; }
  .contact-line { display: flex; align-items: center; gap: 8px; }
  .contact-line svg { width: 12px; height: 12px; fill: var(--brand-blue); flex: none; }
  .address { margin-top: 12px; }
  .card-back { display: flex; align-items: center; justify-content: center; }
  .card-back .brand { color: var(--silver); font-size: 28px; }
  .card-back .brand-mark { background: var(--silver); }
</style>
</head>
<body>
<main class="stage">
  <section class="card card-front" aria-label="Card front">
    <div class="brand"><span class="brand-mark"></span>Stonewell Consulting</div>
    <div class="contact">
      <p class="contact-name">Jordan Avery</p>
      <p class="contact-role">Managing Director</p>
      <p class="contact-line">
        <svg viewBox="0 0 24 24" aria-hidden="true"><path d="M6.6 10.8a15 15 0 0 0 6.6 6.6l2.2-2.2a1 1 0 0 1 1-.25 11.4 11.4 0 0 0 3.6.6 1 1 0 0 1 1 1V20a1 1 0 0 1-1 1A17 17 0 0 1 3 4a1 1 0 0 1 1-1h3.5a1 1 0 0 1 1 1c0 1.25.2 2.45.6 3.6a1 1 0 0 1-.25 1z"/></svg>
        +61 491 570 156</p>
      <p class="contact-line">
        <svg viewBox="0 0 24 24" aria-hidden="true"><path d="M2 5h20v14H2zm2 2v.5l8 5 8-5V7z"/></svg>
        info@stonewell.example</p>
      <p class="contact-line">
        <svg viewBox="0 0 24 24" aria-hidden="true"><path d="M10 14a5 5 0 0 1 0-7l3-3a5 5 0 0 1 7 7l-1.5 1.5-1.4-1.4L18.6 9.6a3 3 0 0 0-4.2-4.2l-3 3a3 3 0 0 0 0 4.2zm4-4a5 5 0 0 1 0 7l-3 3a5 5 0 0 1-7-7l1.5-1.5 1.4 1.4-1.5 1.5a3 3 0 0 0 4.2 4.2l3-3a3 3 0 0 0 0-4.2z"/></svg>
        www.stonewell.example</p>
      <p class="address">12345, Address Goes Here<br>Country Name, 123456.</p>
    </div>
  </section>
  <section class="card card-back" aria-label="Card back">
    <div class="brand"><span class="brand-mark"></span>Stonewell Consulting</div>
  </section>
</main>
</body>
</html>
```